Ready to eat rice packaging design

We need packaging design for pre cooked rice of different types
1. Basmati Rice
2. Brown basmati Rice
3. Jasmine Rice
4. Lemon Rice
5. Rice Pilaf
6. Biryani Rice

Back of the package will have preparation write up and Nutrition chart.

The design should have both natural as well as modern feel to it.

Examples of packages available in market enclosed.

Target Market(s)

National Food and Grocery Stores in USA

Industry/Entity Type

Grocery Store

```html
<!DOCTYPE html>
<html lang="en">
<head>
<meta charset="utf-8">
<title>Meadow Kin Unique Basmati Rice – Pouch Front</title>
<link rel="stylesheet" href="https://fonts.googleapis.com/css2?family=Oswald:wght@400;500;600&family=Montserrat:wght@600;700&family=Antonio:wght@600&display=swap">
<style>
  :root {
    --bg: #f0f0f0;
    --teal: #137f91;
    --teal-dark: #0f6f82;
    --kraft: #d2b896;
    --kraft-light: #dcc4a4;
    --red: #d7201e;
    --ink: #111111;
  }
  * { margin: 0; padding: 0; box-sizing: border-box; }
  html, body {
    width: 1200px; height: 1200px; overflow: hidden;
    background: var(--bg);
  }
  .canvas {
    position: relative; width: 1200px; height: 1200px;
    display: flex; align-items: center; justify-content: center;
  }
  .pouch {
    width: 720px; height: 1000px;
    background: var(--teal);
    padding: 22px 24px 34px;
    border-radius: 6px;
  }
  .pouch-face {
    width: 100%; height: 100%;
    background: linear-gradient(180deg, var(--kraft-light), var(--kraft));
    display: flex; flex-direction: column; align-items: center;
    padding-top: 46px;
    text-align: center;
  }
  .brand-lockup { width: 380px; display: flex; flex-direction: column; align-items: center; }
  .brand-mark {
    width: 46px; height: 46px; background: var(--ink);
    margin-bottom: 18px;
  }
  .rule { width: 100%; height: 2px; background: var(--ink); }
  .brand-name {
    font-family: "Montserrat", sans-serif; font-weight: 700;
    font-size: 22px; letter-spacing: 6px; color: var(--teal-dark);
    padding: 8px 0 6px;
  }
  .story { margin-top: 14px; line-height: 1; }
  .story .headline {
    font-family: "Oswald", sans-serif; font-weight: 600;
    font-size: 54px; color: var(--teal); letter-spacing: -0.5px;
  }
  .story .condensed {
    font-family: "Oswald", sans-serif; font-weight: 500;
    color: var(--ink); letter-spacing: -1px;
  }
  .story .line-country { font-size: 34px; margin-top: 6px; }
  .story .harvest {
    font-family: "Montserrat", sans-serif; font-weight: 700;
    font-size: 48px; color: var(--red); line-height: 1.05; margin-top: 4px;
  }
  .story .line-cool { font-size: 32px; margin-top: 10px; }
  .story .and-tag {
    display: inline-block; margin-top: 14px;
    background: var(--ink); color: var(--kraft-light);
    font-family: "Montserrat", sans-serif; font-weight: 700;
    font-size: 28px; padding: 0 4px; line-height: 1.1;
  }
  .story .line-glow { font-size: 32px; margin-top: 12px; font-weight: 600; }
  .story .christmas {
    font-family: "Montserrat", sans-serif; font-weight: 700;
    font-size: 40px; color: var(--teal); margin-top: 2px;
  }
  .story .line-landscape { font-size: 32px; margin-top: 4px; }
  .product-block { width: 460px; margin-top: 10px; }
  .dash { width: 100%; border-top: 2px dashed var(--teal); }
  .product-brand {
    font-family: "Montserrat", sans-serif; font-weight: 700;
    font-size: 20px; letter-spacing: 7px; color: var(--ink);
    padding: 8px 0;
  }
  .product-name {
    font-family: "Antonio", sans-serif; font-weight: 600;
    line-height: 0.95; padding: 6px 0 4px;
  }
  .product-name .word { display: block; }
  .product-name .unique { font-size: 94px; color: var(--teal-dark); }
  .product-name .basmati { font-size: 96px; color: var(--red); }
  .product-name .rice { font-size: 94px; color: var(--teal); }
</style>
</head>
<body>
<main class="canvas">
  <section class="pouch">
    <div class="pouch-face">
      <header class="brand-lockup">
        <div class="brand-mark"></div>
        <div class="rule"></div>
        <div class="brand-name">MEADOW KIN</div>
        <div class="rule"></div>
      </header>

      <div class="story">
        <p class="headline">NOVEMBER IS AUSPICIOUS</p>
        <p class="condensed line-country">IN SO MANY PARTS OF THE COUNTRY:</p>
        <p class="harvest">THE RICE HARVEST<br>IS ALREADY IN,</p>
        <p class="condensed line-cool">THE WEATHER STARTS TO COOL,</p>
        <span class="and-tag">AND</span>
        <p class="condensed line-glow">THE FESTIVE GLOW WHICH PRECEDES</p>
        <p class="christmas">CHRISTMAS HAS BEGAN</p>
        <p class="condensed line-landscape">TO BRIGHTEN THE LANDSCAPE.</p>
      </div>

      <div class="product-block">
        <div class="dash"></div>
        <div class="product-brand">MEADOW KIN</div>
        <div class="dash"></div>
        <h1 class="product-name">
          <span class="word unique">UNIQUE</span>
          <span class="word basmati">BASMATI</span>
          <span class="word rice">RICE</span>
        </h1>
        <div class="dash"></div>
        <div class="product-brand">MEADOW KIN</div>
        <div class="dash"></div>
      </div>
    </div>
  </section>
</main>
</body>
</html>
```